5-6 page Website Design- Rooted Clarity Course, including 2 videos

We need an elegantly simple and beautiful website for the Rooted Clarity Course (RCC), a 6-month program for founders and leaders of startups who want to shift from Actors to Authors in their leadership.
At a minimum, the website will include:
Home Page
Program Description--Why Actor to Author?
Program Timeline and Structure
Testimonials and Past Clients (this page will include a testimonials video and text)
Team
FAQs
I'd like to see two versions of The Home Page/Landing Page:
1. Just an image with the words
If your startup is growing rapidly,
we can help you do the same.
RCC: The ACTOR to AUTHOR Shift
2. A place for a video describing the program
No payment integration on the website. Just information.
Target Market(s)
Startup founders and senior leaders

```html
<!DOCTYPE html>
<html lang="en">
<head>
<meta charset="utf-8">
<title>Rooted Clarity Course – Website Design</title>
<link href="https://fonts.googleapis.com/css2?family=Montserrat:wght@500;600;700&family=Arimo:wght@400;700&display=swap" rel="stylesheet">
<style>
:root{
  --board:#e1e2e4;
  --navy:#0b4aa8;
  --blue:#1565c0;
  --sky:#229be0;
  --sky-light:#9fd6f5;
  --ink:#111;
  --text:#555;
  --white:#fff;
  --footer:#000;
  --photo-dark:#2c3b4e;
  --photo-mid:#5d6f84;
  --star:#f0a21a;
}
*{box-sizing:border-box;margin:0;padding:0}
html,body{width:1200px;height:2349px;overflow:hidden;background:var(--board)}
body{position:relative;font-family:Arimo,Arial,sans-serif;color:var(--text)}
.page{position:absolute;background:var(--white);overflow:hidden;box-shadow:0 0 3px rgba(0,0,0,.25)}
.page--home{left:23px;top:41px;width:561px;height:2264px}
.page--video{left:602px;top:41px;width:562px;height:874px}
.banner{position:absolute;left:602px;top:942px;width:562px;height:344px;overflow:hidden;box-shadow:0 0 3px rgba(0,0,0,.25)}
.abs{position:absolute}

/* header */
.site-header{position:absolute;left:0;top:0;width:100%;height:54px;background:var(--white)}
.brand{position:absolute;left:53px;top:9px;display:flex;align-items:center;gap:6px}
.brand__dot{width:34px;height:34px;border-radius:50%;background:var(--sky)}
.brand__name{font-family:Montserrat,sans-serif;font-weight:700;font-size:9px;line-height:9.5px;color:var(--navy);text-transform:uppercase;border-left:1px solid var(--navy);padding-left:5px}
.call{position:absolute;right:52px;top:15px;display:flex;align-items:center;gap:6px;font-family:Montserrat,sans-serif;font-weight:600;font-size:9.5px;color:var(--ink)}
.call__icon{width:27px;height:27px;border-radius:50%;background:var(--sky);display:flex;align-items:center;justify-content:center}
.main-nav{position:absolute;left:0;top:54px;width:100%;height:30px;background:var(--blue);display:flex;padding-left:53px}
.main-nav a{font-family:Montserrat,sans-serif;font-weight:600;font-size:6.6px;color:var(--white);text-decoration:none;line-height:30px;padding:0 9.5px}
.main-nav a.is-active{background:var(--sky)}

/* hero */
.hero{position:absolute;left:0;top:84px;width:100%;height:335px}
.hero__photo{position:absolute;inset:0;background:linear-gradient(180deg,var(--photo-mid),var(--photo-dark) 70%,#1e2a38)}
.hero__curve{position:absolute;left:0;bottom:0;width:100%;height:70px}
.hero__title{position:absolute;left:0;width:100%;text-align:center;font-family:Montserrat,sans-serif;font-weight:700;color:var(--white)}
.hero__btn{position:absolute;left:238px;top:242px;width:85px;height:24px;border-radius:12px;background:var(--sky);color:var(--white);font-family:Montserrat,sans-serif;font-weight:500;font-size:7.5px;line-height:24px;text-align:center}
.dots{position:absolute;top:305px;left:50%;transform:translateX(-50%);display:flex;gap:4px}
.dots i{width:6px;height:6px;border-radius:50%;background:var(--white)}
.dots i.on{background:var(--sky)}
.play{position:absolute;left:260px;top:130px;width:44px;height:44px;border-radius:50%;border:2px solid var(--white)}

/* headings & text */
.h-section{font-family:Montserrat,sans-serif;font-weight:600;color:var(--navy);text-transform:uppercase}
.rule{display:block;width:22px;height:1.5px;background:var(--sky);margin-top:8px}
.body-copy{font-size:6.1px;line-height:12px;color:var(--text);text-align:justify}
.btn{position:absolute;height:24px;border-radius:12px;font-family:Montserrat,sans-serif;font-weight:600;font-size:7.5px;line-height:24px;text-align:center}
.btn--solid{background:var(--navy);color:var(--white)}
.btn--outline{border:1.3px solid var(--navy);color:var(--navy);line-height:21px}

.placeholder{position:absolute}

/* timeline */
.timeline{position:absolute;left:0;top:789px;width:100%;height:298px;background:linear-gradient(135deg,#2b9fe6,#1a86d4)}
.timeline__title{position:absolute;top:32px;width:100%;text-align:center;font-family:Montserrat,sans-serif;font-weight:500;font-size:14px;color:var(--white)}
.timeline__title .rule{margin:8px auto 0;background:var(--white)}
.tl-arrow{position:absolute;left:50px;top:158px}
.tl-stem{position:absolute;width:1.5px;background:var(--white)}
.tl-node{position:absolute;width:10px;height:10px;border-radius:50%;background:var(--white)}
.tl-step{position:absolute;color:var(--white);font-size:6px;line-height:11.2px;white-space:nowrap}
.tl-step b{display:block;font-family:Montserrat,sans-serif;font-weight:500;font-size:9.5px;line-height:14px}
.tl-icon{position:absolute;width:24px;height:18px;border:1.2px solid var(--white);border-radius:2px}

/* testimonials */
.testimonials{position:absolute;left:0;top:1485px;width:100%;height:295px;background:var(--blue)}
.card{position:absolute;top:58px;width:147px;height:151px;background:var(--white);text-align:center;padding:24px 9px 0}
.card::after{content:"";position:absolute;left:66px;bottom:-7px;border:7px solid transparent;border-bottom:0;border-top-color:var(--white)}
.stars{color:var(--star);font-size:9px;letter-spacing:1px;margin-bottom:8px}
.card p{font-size:6px;line-height:12px;color:var(--text)}
.avatar{position:absolute;top:224px;width:38px;height:38px;border-radius:50%;background:linear-gradient(#c9b29c,#7a6552);border:2px solid var(--white)}
.person{position:absolute;top:268px;width:147px;text-align:center;font-family:Montserrat,sans-serif;font-weight:600;font-size:7px;color:var(--white)}

/* team */
.member{position:absolute;top:1838px;width:109px;height:137px}
.member__name{position:absolute;left:9px;bottom:14px;font-family:Montserrat,sans-serif;font-weight:600;font-size:7px;color:var(--white)}
.member__line{position:absolute;left:9px;right:9px;bottom:8px;height:1.5px;background:var(--sky)}

/* faq */
.faq{position:absolute;left:0;top:2005px;width:100%;height:80px;background:var(--sky)}
.faq__title{position:absolute;left:69px;top:30px;font-family:Montserrat,sans-serif;font-weight:600;font-size:16px;color:var(--white)}

/* footer */
.footer{position:absolute;left:0;width:100%;background:var(--footer);color:var(--white)}
.footer .brand{left:55px}
.footer .brand__name{color:var(--white);border-color:var(--white)}
.footer .brand__dot{background:var(--white)}
.socials{position:absolute;left:62px;display:flex;gap:3px}
.socials i{width:16px;height:16px;border-radius:50%;border:1px solid var(--white)}
.f-col{position:absolute;font-size:6.2px;line-height:12.8px}
.f-col h4{font-family:Montserrat,sans-serif;font-weight:500;font-size:7.6px;margin-bottom:8px}
.f-col li{list-style:none}
.f-col li::before{content:"→";margin-right:8px}
.f-contact{display:flex;align-items:center;gap:7px;margin-bottom:9px}
.f-contact span.ic{width:14px;height:14px;border-radius:50%;background:#3a3a3a;flex:none}
.email-field{width:102px;height:18px;background:var(--white);color:#888;font-size:5.5px;line-height:18px;padding-left:6px;margin-top:9px}
.submit{display:inline-block;margin-top:6px;background:var(--sky);font-family:Montserrat,sans-serif;font-weight:700;font-size:5.5px;padding:5px 8px}
.footer__rule{position:absolute;left:55px;right:55px;height:1px;background:#333}
.copyright{position:absolute;left:0;width:100%;text-align:center;font-size:6.8px}

/* banner */
.banner__bg{position:absolute;inset:0;background:linear-gradient(160deg,#1b7fd6,#0d4aae 70%,#0b3f9c)}
.banner__photo{position:absolute;inset:0}
.banner .brand{left:18px;top:57px}
.banner .brand__dot{width:58px;height:58px;background:var(--white)}
.banner .brand__name{font-size:16px;line-height:17px;font-weight:600;color:var(--white);border-color:var(--white);padding-left:9px}
.banner__headline{position:absolute;left:18px;top:138px;font-family:Montserrat,sans-serif;font-weight:700;font-size:20.5px;line-height:27px;color:var(--white);text-transform:uppercase}
.banner__headline em{font-style:normal;color:#44b3f0}
.banner__tag{position:absolute;left:15px;top:258px;font-family:Montserrat,sans-serif;font-weight:700;font-size:10.5px;color:var(--white)}
</style>
</head>
<body>

<!-- ================= HOME PAGE (image hero) ================= -->
<section class="page page--home">
  <header class="site-header">
    <div class="brand"><span class="brand__dot"></span><span class="brand__name">Rooted<br>Clarity<br>Course</span></div>
    <div class="call"><span class="call__icon"><svg width="11" height="11" viewBox="0 0 24 24"><path fill="#fff" d="M6.6 10.8a15 15 0 0 0 6.6 6.6l2.2-2.2c.3-.3.7-.4 1-.2 1.1.4 2.3.6 3.6.6.6 0 1 .4 1 1V20c0 .6-.4 1-1 1A17 17 0 0 1 3 4c0-.6.4-1 1-1h3.5c.6 0 1 .4 1 1 0 1.3.2 2.5.6 3.6.1.3 0 .7-.2 1z"/></svg></span>CALL US : +1 555 010 2040</div>
  </header>
  <nav class="main-nav">
    <a class="is-active">HOME</a><a>PROGRAM DESCRIPTION</a><a>PROGRAM TIMELINE &amp; STRUCTURE</a><a>TESTIMONIALS &amp; PAST</a><a>TEAM</a><a>FAQS</a>
  </nav>

  <div class="hero">
    <div class="hero__photo" role="img" aria-label="Photo of a cheering team of colleagues celebrating in an office"></div>
    <div class="hero__title" style="top:164px;font-size:18px">ROOTED CLARITY COURSE</div>
    <div class="hero__title" style="top:190px;font-size:18px;color:var(--sky)">6-MONTH PROGRAM</div>
    <div class="hero__btn">GET IN TOUCH</div>
    <div class="dots"><i></i><i class="on"></i><i></i></div>
    <svg class="hero__curve" viewBox="0 0 561 70" preserveAspectRatio="none"><path d="M0 18 Q280 90 561 18 V70 H0Z" fill="#fff"/><path d="M0 18 Q280 90 561 18" fill="none" stroke="#1e8fdb" stroke-width="3"/></svg>
  </div>

  <!-- program description -->
  <div class="placeholder" style="left:41px;top:577px;width:187px;height:171px;border:7px solid var(--sky-light);border-top:none;border-right:none"></div>
  <div class="placeholder" style="left:221px;top:728px;width:7px;height:20px;background:var(--sky-light)"></div>
  <div class="placeholder" role="img" aria-label="Photo of colleagues laughing together in a bright office" style="left:70px;top:467px;width:173px;height:217px;background:linear-gradient(160deg,#8a9aa8,#4a5866)"></div>
  <div class="placeholder" role="img" aria-label="Photo of a team meeting around a conference table" style="left:164px;top:586px;width:114px;height:137px;background:linear-gradient(160deg,#c7ccd2,#6c7580);border:3px solid #fff"></div>
  <div class="abs" style="left:296px;top:484px;width:215px">
    <h2 class="h-section" style="font-size:14px">Program Description<span class="rule"></span></h2>
    <p class="body-copy" style="margin-top:13px">If you want to be busy and anxious, practice busy anxiousness. If you want to be calm and centered, practice it. It's as simple as that." (Mara Ellison, Westbrook Institute mindfulness teacher and researcher)</p>
    <p class="body-copy" style="margin-top:12px">Well thanks Mara, sounds pretty simple…but what about when I've got 11 back-to-back meetings, a board meeting to prepare for with investors who have sky-high expectations, 6 new hires to onboard and 16 more to find, and–not least–a product to improve for the customers we are trying to serve and retain–only to wake up, rinse (maybe) and repeat tomorrow?? (We didn't even mention the team chat and email messages mounting in the background.) How could I possibly exit "busy anxiousness" and practice calm centeredness amidst this chaos? (Notice what you feel just reading tighten a bit?) Calm sounds nice–for vacation! I want results.</p>
  </div>
  <div class="btn btn--solid" style="left:297px;top:688px;width:76px">READ MORE</div>

  <!-- timeline -->
  <div class="timeline">
    <div class="timeline__title">PROGRAM TIMELINE &amp; STRUCTURE<span class="rule"></span></div>

    <svg class="tl-arrow" width="470" height="24" viewBox="0 0 470 24"><line x1="5" y1="12" x2="462" y2="12" stroke="#fff" stroke-width="3"/><path d="M450 3 L464 12 L450 21" fill="none" stroke="#fff" stroke-width="3"/></svg>

    <!-- stems -->
    <i class="tl-stem" style="left:126px;top:85px;height:85px"></i>
    <i class="tl-stem" style="left:278px;top:85px;height:85px"></i>
    <i class="tl-stem" style="left:427px;top:82px;height:88px"></i>
    <i class="tl-stem" style="left:54px;top:170px;height:84px"></i>
    <i class="tl-stem" style="left:203px;top:170px;height:84px"></i>
    <i class="tl-stem" style="left:353px;top:170px;height:84px"></i>

    <!-- nodes on main line -->
    <i class="tl-node" style="left:50px;top:165px"></i>
    <i class="tl-node" style="left:122px;top:165px"></i>
    <i class="tl-node" style="left:199px;top:165px"></i>
    <i class="tl-node" style="left:274px;top:165px"></i>
    <i class="tl-node" style="left:349px;top:165px"></i>
    <i class="tl-node" style="left:423px;top:165px"></i>
    <!-- end nodes -->
    <i class="tl-node" style="left:122px;top:80px"></i>
    <i class="tl-node" style="left:274px;top:80px"></i>
    <i class="tl-node" style="left:423px;top:77px"></i>
    <i class="tl-node" style="left:50px;top:249px"></i>
    <i class="tl-node" style="left:199px;top:249px"></i>
    <i class="tl-node" style="left:349px;top:249px"></i>

    <!-- upper steps -->
    <div class="tl-step" style="left:137px;top:78px"><b>Month 2</b>Week 1: 1st Retreat<br>("Leading Yourself")<br>Week 2: 1on1 Exec<br>Coaching Session<br>Week 4: Workshop</div>
    <div class="tl-step" style="left:289px;top:78px"><b>Month 4</b>Week 2: 1on1 Exec<br>Coaching Session</div>
    <div class="tl-step" style="left:438px;top:75px"><b>Month 6</b>Week 2: 1on1 Exec<br>Coaching Session<br>Week 4: Concluding<br>Workshop<br>Week 5: Concluding 1on1</div>

    <!-- lower steps -->
    <div class="tl-step" style="left:66px;top:187px"><b>Month 1</b>Week 1: Kickoff<br>Orientation Workshop<br>Week 2: 1on1 Exec<br>Coaching Session<br>Week 3: Workshop</div>
    <div class="tl-step" style="left:215px;top:187px"><b>Month 3</b>Week 2: 1on1 Exec<br>Coaching Session<br>Week 4: Workshop</div>
    <div class="tl-step" style="left:366px;top:187px"><b>Month 5</b>Week 1: 2nd Retreat<br>("Leading Others, Leading<br>Relationships")<br>Week 2: 1on1 Exec<br>Coaching Session<br>Week 4: Workshop</div>

    <!-- small icons -->
    <i class="tl-icon" style="left:45px;top:137px"></i>
    <i class="tl-icon" style="left:196px;top:137px"></i>
    <i class="tl-icon" style="left:342px;top:139px"></i>
    <i class="tl-icon" style="left:115px;top:182px"></i>
    <i class="tl-icon" style="left:269px;top:180px"></i>
    <i class="tl-icon" style="left:420px;top:178px;width:18px;height:23px"></i>
  </div>

  <!-- why retreats / coaching -->
  <div class="placeholder" role="img" aria-label="Line illustration of a head in profile with a lightbulb inside" style="left:82px;top:1124px;width:166px;height:155px;background:radial-gradient(circle,#d7ebfa,#fff 70%)"></div>
  <div class="abs" style="left:281px;top:1133px;width:230px">
    <h3 class="h-section" style="font-size:12px">Why Retreats?<span class="rule"></span></h3>
    <p class="body-copy" style="margin-top:12px">The retreat environment creates an immersive experience, co-created by the group. The sharp distinction from the fast pace of everyday startup life helps participants stand outside their everyday habits and evaluate which ones they want to change. Furthermore, just like in learning a language, immersion is the most powerful context for learning and ingraining new habits.</p>
  </div>
  <div class="btn btn--outline" style="left:281px;top:1242px;width:71px">READ MORE</div>

  <div class="abs" style="left:53px;top:1334px;width:230px">
    <h3 class="h-section" style="font-size:12px">Why Coaching?<span class="rule"></span></h3>
    <p class="body-copy" style="margin-top:12px">At the same time, personalization and coaching take us to a deeper level, helping explore and grow some of the inner game growth areas that emerge in the interpersonal interactions within the group. Coaching is a powerful context for exploring the mindset shifts in moving from Actor to Author.</p>
  </div>
  <div class="btn btn--outline" style="left:53px;top:1431px;width:71px">READ MORE</div>
  <div class="placeholder" role="img" aria-label="Line illustration of a coach with two people and checkmark speech bubbles" style="left:324px;top:1309px;width:146px;height:159px;background:radial-gradient(circle,#d7ebfa,#fff 70%)"></div>

  <!-- testimonials -->
  <div class="testimonials">
    <div class="timeline__title" style="top:22px;font-weight:600;font-size:14px">OUR TESTIMONIALS</div>
    <div class="card" style="left:53px"><div class="stars">☆☆☆☆☆</div><p>Sed ut perspiciatis unde omnis iste natus error sit voluptatem accusantium doloremque laudantium, totam rem aperiam, eaque ipsa quae ab illo inventore veritatis et quasi arc hitecto beatae vitae dicta sunt explicabo. Ne mo enim ipsam voluptatem quia voluptas vol uptatem sequi nesciunt.</p></div>
    <div class="card" style="left:208px"><div class="stars">☆☆☆☆☆</div><p>Sed ut perspiciatis unde omnis iste natus error sit voluptatem accusantium doloremque laudantium, totam rem aperiam, eaque ipsa quae ab illo inventore veritatis et quasi arc hitecto beatae vitae dicta sunt explicabo. Ne mo enim ipsam voluptatem quia voluptas vol uptatem sequi nesciunt.</p></div>
    <div class="card" style="left:363px"><div class="stars">☆☆☆☆☆</div><p>Sed ut perspiciatis unde omnis iste natus error sit voluptatem accusantium doloremque laudantium, totam rem aperiam, eaque ipsa quae ab illo inventore veritatis et quasi arc hitecto beatae vitae dicta sunt explicabo. Ne mo enim ipsam voluptatem quia voluptas vol uptatem sequi nesciunt.</p></div>
    <div class="avatar" role="img" aria-label="Client portrait" style="left:107px"></div>
    <div class="avatar" role="img" aria-label="Client portrait" style="left:262px"></div>
    <div class="avatar" role="img" aria-label="Client portrait" style="left:417px"></div>
    <div class="person" style="left:53px">ALEX RIVERA</div><div class="person" style="left:208px">ALEX RIVERA</div><div class="person" style="left:363px">ALEX RIVERA</div>
  </div>

  <!-- team -->
  <h2 class="h-section abs" style="left:0;top:1798px;width:100%;text-align:center;font-size:14px">Our Team<span class="rule" style="margin:7px auto 0"></span></h2>
  <div class="member" role="img" aria-label="Team member portrait" style="left:53px;background:linear-gradient(#b7b3ae,#3a3633)"><span class="member__name">ALEX RIVERA</span><span class="member__line"></span></div>
  <div class="member" role="img" aria-label="Team member portrait with bio" style="left:168px;background:linear-gradient(#c8c8c8,#2b2b2b)">
    <span class="member__name" style="bottom:48px">ALEX RIVERA</span>
    <span class="member__line" style="bottom:41px;background:#fff"></span>
    <span class="abs" style="left:9px;bottom:18px;width:92px;font-size:5.6px;line-height:9px;color:#fff">Sed ut perspiciatis unde omnis iste natus error sit voluptatem</span>
    <span class="abs" style="left:9px;bottom:8px;display:flex;gap:3px"><i style="width:5px;height:5px;border-radius:50%;background:#fff"></i><i style="width:5px;height:5px;border-radius:50%;background:#fff"></i><i style="width:5px;height:5px;border-radius:50%;background:#fff"></i></span>
  </div>
  <div class="member" role="img" aria-label="Team member portrait" style="left:284px;background:linear-gradient(#dcdcdc,#b8962a)"><span class="member__name">ALEX RIVERA</span><span class="member__line"></span></div>
  <div class="member" role="img" aria-label="Team member portrait" style="left:400px;background:linear-gradient(#cfd4d9,#3c5e96)"><span class="member__name">ALEX RIVERA</span><span class="member__line"></span></div>

  <!-- faq -->
  <div class="faq">
    <div class="faq__title">FREQUENTLY ASKED QUESTIONS</div>
    <div class="btn btn--solid" style="left:393px;top:27px;width:93px;height:26px;line-height:26px;border-radius:13px">READ MORE</div>
  </div>

  <!-- footer -->
  <footer class="footer" style="top:2085px;height:179px">
    <div class="brand" style="top:48px"><span class="brand__dot"></span><span class="brand__name">Rooted<br>Clarity<br>Course</span></div>
    <div class="socials" style="top:97px"><i></i><i></i><i></i><i></i><i></i></div>
    <div class="f-col" style="left:187px;top:33px"><h4>QUICK LINKS</h4><ul><li>HOME</li><li>PROGRAM DESCRIPTION</li><li>PROGRAM TIMELINE</li><li>TESTIMONIALS</li><li>TEAM</li><li>FAQS</li></ul></div>
    <div class="f-col" style="left:297px;top:33px;width:100px"><h4>CONTACT</h4>
      <div class="f-contact"><span class="ic"></span>+1 555 010 2040</div>
      <div class="f-contact"><span class="ic"></span>hello@rootedclarity.example</div>
      <div class="f-contact" style="line-height:10px"><span class="ic"></span>#154 lore Ipsum dummy<br>Loram ipsum</div>
    </div>
    <div class="f-col" style="left:407px;top:33px;width:105px;line-height:10px"><h4>NEWSLETTER</h4>Sed ut perspiciatis unde omnis us error sit voluptatem<div class="email-field">Email :</div><span class="submit">SUBMIT</span></div>
    <div class="footer__rule" style="top:146px"></div>
    <div class="copyright" style="top:156px">© Copyrights 2022 Company Name.All Rights Reserved.</div>
  </footer>
</section>

<!-- ================= HOME PAGE (video hero) ================= -->
<section class="page page--video">
  <header class="site-header">
    <div class="brand"><span class="brand__dot"></span><span class="brand__name">Rooted<br>Clarity<br>Course</span></div>
    <div class="call"><span class="call__icon"><svg width="11" height="11" viewBox="0 0 24 24"><path fill="#fff" d="M6.6 10.8a15 15 0 0 0 6.6 6.6l2.2-2.2c.3-.3.7-.4 1-.2 1.1.4 2.3.6 3.6.6.6 0 1 .4 1 1V20c0 .6-.4 1-1 1A17 17 0 0 1 3 4c0-.6.4-1 1-1h3.5c.6 0 1 .4 1 1 0 1.3.2 2.5.6 3.6.1.3 0 .7-.2 1z"/></svg></span>CALL US : +1 555 010 2040</div>
  </header>
  <nav class="main-nav">
    <a class="is-active">HOME</a><a>PROGRAM DESCRIPTION</a><a>PROGRAM TIMELINE &amp; STRUCTURE</a><a>TESTIMONIALS &amp; PAST</a><a>TEAM</a><a>FAQS</a>
  </nav>
  <div class="hero" style="height:345px">
    <div class="hero__photo" role="img" aria-label="Video still of business partners shaking hands across a meeting table"></div>
    <div class="play"><svg width="40" height="40" viewBox="0 0 40 40"><path d="M16 12 L28 20 L16 28Z" fill="#fff"/></svg></div>
    <div class="hero__title" style="top:180px;font-size:18px;line-height:23px">ROOTED CLARITY<br>COURSE</div>
    <div class="dots" style="top:305px"><i></i><i class="on"></i><i></i></div>
    <svg class="hero__curve" viewBox="0 0 561 70" preserveAspectRatio="none" style="bottom:0"><path d="M0 8 Q280 80 561 8 V70 H0Z" fill="#fff"/><path d="M0 8 Q280 80 561 8" fill="none" stroke="#1e8fdb" stroke-width="3"/></svg>
  </div>
  <div class="abs" style="left:100px;top:455px;width:362px;text-align:center">
    <h2 class="h-section" style="font-size:14px">Program Description<span class="rule" style="margin:7px auto 0"></span></h2>
    <p class="body-copy" style="margin-top:12px;text-align:center">If you want to be busy and anxious, practice busy anxiousness. If you want to be calm and centered, practice it. It's as simple as that." (Mara Ellison, Westbrook Institute mindfulness teacher and researcher)</p>
    <p class="body-copy" style="margin-top:13px;text-align:center">Well thanks Mara, sounds pretty simple…but what about when I've got 11 back-to-back meetings, a board meeting to prepare for with investors who have sky-high expectations, 6 new hires to onboard and 16 more to find, and–not least–a product to improve for the customers we are trying to serve and retain–only to wake up, rinse (maybe) and repeat tomorrow?? (We didn't even mention the team chat and email messages mounting in the background.) How could I possibly exit "busy anxiousness" and practice calm centeredness amidst this chaos? (Notice what you feel just reading tighten a bit?) Calm sounds nice–for vacation! I want results.</p>
    <p class="body-copy" style="margin-top:13px;text-align:center">There is a way, not to perfection and a stress-less existence, but rather a way of working, being, and leading from a deeper calm that creates enough space to harness the remaining (necessary) stress as fuel towards your goals.</p>
  </div>
  <div class="btn btn--solid" style="left:243px;top:638px;width:76px">READ MORE</div>
  <footer class="footer" style="top:696px;height:178px">
    <div class="brand" style="top:48px"><span class="brand__dot"></span><span class="brand__name">Rooted<br>Clarity<br>Course</span></div>
    <div class="socials" style="top:97px"><i></i><i></i><i></i><i></i><i></i></div>
    <div class="f-col" style="left:187px;top:34px"><h4>QUICK LINKS</h4><ul><li>HOME</li><li>PROGRAM DESCRIPTION</li><li>PROGRAM TIMELINE</li><li>TESTIMONIALS</li><li>TEAM</li><li>FAQS</li></ul></div>
    <div class="f-col" style="left:297px;top:34px;width:100px"><h4>CONTACT</h4>
      <div class="f-contact"><span class="ic"></span>+1 555 010 2040</div>
      <div class="f-contact"><span class="ic"></span>hello@rootedclarity.example</div>
      <div class="f-contact" style="line-height:10px"><span class="ic"></span>#154 lore Ipsum dummy<br>Loram ipsum</div>
    </div>
    <div class="f-col" style="left:407px;top:34px;width:105px;line-height:10px"><h4>NEWSLETTER</h4>Sed ut perspiciatis unde omnis us error sit voluptatem<div class="email-field">Email :</div><span class="submit">SUBMIT</span></div>
    <div class="footer__rule" style="top:144px"></div>
    <div class="copyright" style="top:157px">© Copyrights 2022 Company Name.All Rights Reserved.</div>
  </footer>
</section>

<!-- ================= LANDING BANNER ================= -->
<section class="banner">
  <div class="banner__bg"></div>
  <svg class="banner__photo" viewBox="0 0 562 344" preserveAspectRatio="none" role="img" aria-label="Photo of a presenter leading a team meeting, tinted blue">
    <defs><linearGradient id="meeting-tint" x1="0" y1="0" x2="1" y2="1"><stop offset="0" stop-color="#5aa6e6"/><stop offset="1" stop-color="#1a5fb8"/></linearGradient></defs>
    <path d="M287 0 Q215 150 290 344 H562 V0Z" fill="url(#meeting-tint)"/>
    <path d="M287 0 Q215 150 290 344" fill="none" stroke="#fff" stroke-width="3"/>
  </svg>
  <div class="brand"><span class="brand__dot"></span><span class="brand__name">Rooted<br>Clarity<br>Course</span></div>
  <div class="banner__headline">If your <em>startup is</em><br><em>growing</em> rapidly<br>we can help you<br>do the <em>same.</em></div>
  <div class="banner__tag">RCC : THE ACTOR TO AUTHOR SHIFT</div>
</section>

</body>
</html>
```